Toravel Project Consulting

I need a logo and business card design for a small business operating in the management consulting and contractor space, predominantly in local and state government. I specialise in project management, financial consulting, people and culture, procurement, ICT transformation and contracting for corporate support areas of organisations.

Industry/Entity Type

Business

```html
<!DOCTYPE html>
<html lang="en">
<head>
<meta charset="utf-8">
<title>Toravel Project Consulting – Business Card</title>
<link rel="stylesheet" href="https://fonts.googleapis.com/css2?family=Roboto:wght@400;700&display=swap">
<style>
  :root {
    --backdrop: #1c1c1e;
    --card: #ffffff;
    --brand-blue: #1f73c1;
    --brand-light: #7fb4e0;
    --ink: #1d1d1f;
    --muted: #555a60;
  }
  * { box-sizing: border-box; margin: 0; padding: 0; }
  html, body {
    width: 1200px; height: 964px; overflow: hidden;
    background: var(--backdrop);
    font-family: "Roboto", Arial, sans-serif;
  }
  .stage {
    width: 1200px; height: 964px;
    display: flex; flex-direction: column;
    align-items: center; justify-content: center; gap: 56px;
  }
  .card {
    position: relative;
    width: 700px; height: 400px;
    background: var(--card);
    border-radius: 26px;
    overflow: hidden;
  }
  .brand {
    display: flex; align-items: center; gap: 14px;
    color: var(--brand-blue);
    font-weight: 700;
    font-size: 30px;
    letter-spacing: 0.5px;
  }
  .brand-mark {
    width: 22px; height: 22px;
    background: var(--brand-blue);
  }
  /* back side */
  .card-back {
    display: flex; flex-direction: column;
    align-items: center; justify-content: center; gap: 26px;
  }
  .card-back .website { font-size: 20px; color: var(--muted); }
  .website .domain { color: var(--brand-blue); }
  /* front side */
  .card-front .brand { position: absolute; left: 44px; top: 48px; }
  .wave { position: absolute; left: 0; top: 0; }
  .contact {
    position: absolute; right: 50px; top: 150px;
    text-align: right; color: var(--ink);
  }
  .contact .name { font-size: 28px; font-weight: 700; color: var(--brand-blue); line-height: 1.1; }
  .contact .role { font-size: 18px; font-weight: 700; margin-bottom: 6px; }
  .contact .address { font-size: 18px; line-height: 1.3; margin-bottom: 4px; }
  .contact .line {
    display: flex; justify-content: flex-end; align-items: center; gap: 12px;
    font-size: 18px; line-height: 1.4;
  }
  .contact .icon { width: 18px; height: 18px; flex: none; }
</style>
</head>
<body>
<main class="stage">

  <section class="card card-back" aria-label="Card back">
    <div class="brand"><span class="brand-mark"></span>Toravel Project Consulting</div>
    <p class="website">www.<span class="domain">toravelconsulting</span>.com</p>
  </section>

  <section class="card card-front" aria-label="Card front">
    <svg class="wave" width="700" height="400" viewBox="0 0 700 400" aria-hidden="true">
      <defs>
        <linearGradient id="bandFill" x1="0" y1="0" x2="1" y2="0">
          <stop offset="0" stop-color="#1f73c1"/>
          <stop offset="0.45" stop-color="#7fb4e0"/>
          <stop offset="0.75" stop-color="#2f80c8"/>
          <stop offset="1" stop-color="#1f73c1"/>
        </linearGradient>
      </defs>
      <path d="M0,300 C220,365 470,352 700,405 L700,400 L0,400 Z" fill="url(#bandFill)"/>
      <path d="M0,284 C220,350 470,338 700,392" fill="none" stroke="#ffffff" stroke-width="6"/>
      <path d="M0,274 C220,340 470,328 700,382" fill="none" stroke="#7fb4e0" stroke-width="4"/>
    </svg>

    <div class="brand"><span class="brand-mark"></span>Toravel Project Consulting</div>

    <div class="contact">
      <p class="name">Daniel Hartley</p>
      <p class="role">Director</p>
      <p class="address">14 Harbour Lane<br>Northvale NSW 2190</p>
      <p class="line">(02) 555 0184
        <svg class="icon" viewBox="0 0 18 18" aria-hidden="true"><rect x="4" y="1" width="10" height="16" rx="2" fill="none" stroke="#1f73c1" stroke-width="1.6"/><circle cx="9" cy="14" r="1" fill="#1f73c1"/></svg>
      </p>
      <p class="line">info@toravelconsulting.com
        <svg class="icon" viewBox="0 0 18 18" aria-hidden="true"><rect x="1" y="4" width="16" height="11" fill="#1f73c1"/><path d="M1,4 L9,11 L17,4" fill="none" stroke="#fff" stroke-width="1.4"/></svg>
      </p>
      <p class="line"><span>www.<span style="color:var(--brand-blue)">toravelconsulting</span>.com</span>
        <svg class="icon" viewBox="0 0 18 18" aria-hidden="true"><circle cx="9" cy="9" r="8" fill="#1f73c1"/><path d="M1,9 H17 M9,1 V17 M3,5 H15 M3,13 H15" stroke="#fff" stroke-width="1"/><ellipse cx="9" cy="9" rx="3.5" ry="8" fill="none" stroke="#fff" stroke-width="1"/></svg>
      </p>
    </div>
  </section>

</main>
</body>
</html>
```